Introduction Post card

Harbourline Doors
27 Varnel Road
Ruthven Ontario
Gus@harbourlinedoorsco.net
519-555-0143

Dear Leamington Residents

We are excited to announce the launch of Harbourline Doors, your new local source for high-quality windows, doors, and garage doors! As a dedicated member of this community, we are committed to providing exceptional products and services that enhance the beauty and functionality of your home or business.

At Harbourline Doors, we understand that choosing the right windows and doors is essential for energy efficiency, security, and style. That’s why we offer a wide selection of premium products tailored to meet your unique needs. Our expert team is here to guide you through the selection process, ensuring you find the perfect fit for your space.

Our services don’t stop at providing quality products. We pride ourselves on our professional installation process, ensuring that every project is completed with precision and care. Customer satisfaction is our top priority, and we strive to exceed your expectations with every interaction.

We invite you to visit our showroom or contact us to learn more about our offerings. Whether you’re looking to upgrade your home’s curb appeal or enhance its security, we are here to help. Together, let’s make our community a more beautiful place!

Thank you for considering Harbourline Doors for your window, door, and garage door needs. We look forward to serving you!

Warm regards,

Gus
Sales Manager
Harbourline Doors
https://harbourlinedoorsco.net/

```html
<!DOCTYPE html>
<html lang="en">
<head>
<meta charset="utf-8">
<title>Harbourline Doors – Introduction Postcard</title>
<link rel="stylesheet" href="https://fonts.googleapis.com/css2?family=Fira+Sans+Condensed:wght@600&family=Raleway:wght@400;500&family=Outfit:wght@400;500&family=Kaushan+Script&display=swap">
<style>
  :root {
    --backdrop: #a7a7a7;
    --charcoal: #3a3935;
    --charcoal-deep: #31302c;
    --paper: #ffffff;
    --ink: #2b2a27;
    --accent: #e05a28;
    --photo-sky: #9cc1e2;
    --photo-lawn: #5a9c34;
    --portrait: #5c5f63;
  }
  * { margin: 0; padding: 0; box-sizing: border-box; }
  html, body { width: 1200px; height: 1200px; overflow: hidden; }
  body { background: var(--backdrop); position: relative; font-family: "Raleway", sans-serif; color: var(--ink); }

  .postcard-front {
    position: absolute; left: 83px; top: 81px; width: 689px; height: 500px;
    background: var(--charcoal); overflow: hidden;
  }
  .front-corner-paper { position: absolute; left: 0; top: 0; width: 60px; height: 200px; background: var(--paper); }
  .front-corner-band {
    position: absolute; left: 0; top: 158px; width: 51px; height: 342px;
    background: var(--charcoal); border-top-left-radius: 51px;
  }
  .letter-panel { position: absolute; left: 51px; top: 0; width: 320px; height: 452px; background: var(--paper); }
  .signoff-panel { position: absolute; left: 371px; top: 239px; width: 269px; height: 213px; background: var(--paper); }
  .house-photo {
    position: absolute; left: 371px; top: 51px; width: 269px; height: 188px;
    background: linear-gradient(180deg, var(--photo-sky) 0%, var(--photo-lawn) 100%);
  }

  .brand-name {
    font-family: "Fira Sans Condensed", sans-serif; font-weight: 600;
    white-space: nowrap; line-height: 1;
  }
  .front-brand {
    position: absolute; left: 41px; top: 23px; z-index: 2;
    display: flex; align-items: center; gap: 9px;
  }
  .front-brand .brand-mark { width: 46px; height: 46px; background: var(--charcoal); border-radius: 4px; flex: none; }
  .front-brand .brand-name { color: var(--accent); font-size: 21px; }

  .greeting {
    position: absolute; left: 74px; top: 92px; font-family: "Kaushan Script", cursive;
    font-size: 22px; font-weight: 400; color: var(--accent); white-space: nowrap;
  }
  .letter-body {
    position: absolute; left: 77px; top: 132px; width: 280px; height: 292px; overflow: hidden;
    font-size: 10.5px; line-height: 12.7px;
  }
  .letter-body p + p { margin-top: 12.7px; }

  .thanks-title {
    position: absolute; left: 380px; top: 254px; font-family: "Kaushan Script", cursive;
    font-size: 27px; font-weight: 400; color: var(--ink); white-space: nowrap;
  }
  .thanks-body { position: absolute; left: 383px; top: 294px; width: 232px; font-size: 10.4px; line-height: 12.7px; }
  .closing { position: absolute; left: 384px; top: 343px; font-family: "Outfit", sans-serif; font-size: 12.5px; }
  .portrait {
    position: absolute; left: 379px; top: 365px; width: 64px; height: 64px; border-radius: 50%;
    background: var(--portrait);
    border: 1.5px solid var(--accent); box-shadow: inset 0 0 0 2px var(--paper);
  }
  .signer { position: absolute; left: 454px; top: 371px; font-family: "Outfit", sans-serif; line-height: 1.2; }
  .signer-name { font-size: 13.5px; }
  .signer-role { font-size: 7.4px; color: var(--accent); margin-bottom: 2px; }
  .signer-contact { font-size: 8.4px; font-weight: 500; }

  .contact-bar {
    position: absolute; left: 0; top: 461px; width: 689px; height: 24px;
    font-family: "Outfit", sans-serif; font-weight: 500; color: var(--paper); font-size: 13px;
  }
  .contact-item { position: absolute; top: 0; height: 24px; display: flex; align-items: center; gap: 5px; white-space: nowrap; }
  .contact-item svg { width: 12px; height: 12px; flex: none; }
  .contact-divider { position: absolute; top: 1px; width: 1px; height: 22px; background: var(--paper); }

  .postcard-back {
    position: absolute; left: 404px; top: 625px; width: 691px; height: 501px; background: var(--charcoal-deep);
  }
  .back-brand { position: absolute; left: 0; width: 691px; top: 286px; text-align: center; color: var(--paper); font-size: 36px; }
  .back-web {
    position: absolute; left: 0; width: 691px; top: 410px; display: flex; justify-content: center; align-items: center; gap: 8px;
    font-family: "Outfit", sans-serif; font-size: 13.5px; color: var(--paper); letter-spacing: 0.45em;
  }
  .back-web svg { width: 14px; height: 14px; }
</style>
</head>
<body>

<section class="postcard-front">
  <div class="front-corner-paper"></div>
  <div class="front-corner-band"></div>
  <div class="letter-panel"></div>
  <div class="signoff-panel"></div>
  <div class="house-photo" role="img" aria-label="Photo of a modern two-storey house with wood cladding, green lawn and blue sky"></div>

  <div class="front-brand">
    <span class="brand-mark"></span>
    <span class="brand-name">HARBOURLINE DOORS</span>
  </div>

  <h1 class="greeting">Dear Leamington Residents</h1>

  <div class="letter-body">
    <p>We are excited to announce the launch of Harbourline Doors, your new local source for high-quality windows, doors, and garage doors! As a dedicated member of this community, we are committed to providing exceptional products and services that enhance the beauty and functionality of your home or business.</p>
    <p>At Harbourline Doors, we understand that choosing the right windows and doors is essential for energy efficiency, security, and style. That's why we offer a wide selection of premium products tailored to meet your unique needs. Our expert team is here to guide you through the selection process, ensuring you find the perfect fit for your space.</p>
    <p>Our services don't stop at providing quality products. We pride ourselves on our professional installation process, ensuring that every project is completed with precision and care. Customer satisfaction is our top priority, and we strive to exceed your expectations with every interaction.</p>
    <p>We invite you to visit our showroom or contact us to learn more about our offerings. Whether you're looking to upgrade your home's curb appeal or enhance its security, we are here to help. Together, let's make our community a more beautiful place!</p>
  </div>

  <h2 class="thanks-title">Thank you</h2>
  <p class="thanks-body">for considering Harbourline Doors for your window, door, and garage door needs. We look forward to serving you!</p>
  <p class="closing">Warm regards,</p>
  <div class="portrait" role="img" aria-label="Portrait photo of the sales manager"></div>
  <div class="signer">
    <div class="signer-name">Gus Halden</div>
    <div class="signer-role">Sales Manager</div>
    <div class="signer-contact">Gus@harbourlinedoorsco.net</div>
    <div class="signer-contact">www.harbourlinedoorsco.net</div>
  </div>

  <div class="contact-bar">
    <div class="contact-item" style="left:72px">
      <svg viewBox="0 0 24 24"><path fill="var(--accent)" d="M12 1.5a8 8 0 0 0-8 8c0 6 8 13 8 13s8-7 8-13a8 8 0 0 0-8-8zm0 11a3 3 0 1 1 0-6 3 3 0 0 1 0 6z"/></svg>
      <span>27 Varnel Road Ruthven Ontario</span>
    </div>
    <span class="contact-divider" style="left:298px"></span>
    <div class="contact-item" style="left:318px">
      <svg viewBox="0 0 24 24"><path fill="var(--accent)" d="M6.6 2.5l3 3.2-1.8 2.6c1.2 2.9 3.2 5 6 6.3l2.6-1.8 3.2 3-1.6 3.4c-.4.8-1.3 1.2-2.2 1C8.6 18.4 4.2 13.5 2.6 6.4c-.2-.9.2-1.8 1-2.2z"/></svg>
      <span>519-555-0143</span>
    </div>
    <span class="contact-divider" style="left:433px"></span>
    <div class="contact-item" style="left:453px">
      <svg viewBox="0 0 24 24" fill="none" stroke="var(--accent)" stroke-width="1.6"><circle cx="12" cy="12" r="10"/><ellipse cx="12" cy="12" rx="4.5" ry="10"/><path d="M2 12h20M4 6.5h16M4 17.5h16"/></svg>
      <span>www.harbourlinedoorsco.net</span>
    </div>
  </div>
</section>

<section class="postcard-back">
  <span class="brand-name back-brand">HARBOURLINE DOORS</span>
  <div class="back-web">
    <svg viewBox="0 0 24 24" fill="none" stroke="var(--accent)" stroke-width="1.6"><circle cx="12" cy="12" r="10"/><ellipse cx="12" cy="12" rx="4.5" ry="10"/><path d="M2 12h20M4 6.5h16M4 17.5h16"/></svg>
    <span>WWW.HARBOURLINEDOORSCO.NET</span>
  </div>
</section>

</body>
</html>
```